Card design for Heating and Cooling company

this is for a heating and cooling company we recently updated our logo and need to update our cards. We attached our logo so you can incorporate it into the card. We specialize in residential and commercial furnace and air condition repairs. Have been in business since 2014.

Phone number 555.284.9137

We need the following phrases
:Repairs, Installations, and maintenance
:Quality work at reasonable prices
:residential/commercial
:Licensed &Insured
:Email Pinegrovehvac47@mailbox-example.com
Name: Teodor K (Ted)
Also on back side I would like my logo with wording :Thank you for your business and refferal

Industry/Entity Type

Hvac

Contact Information for Business Card

:residential/commercial
:Licensed & Insured
Name: Teodor K (Ted)
Number:555.284.9136

Requirements
Must have
• Blue and red colors
Nice to have
• Maybe a pic of a furnace or air conditioner

```html
<!DOCTYPE html>
<html lang="en">
<head>
<meta charset="utf-8">
<title>Pinegrove Heating &amp; Cooling – Business Card</title>
<link href="https://fonts.googleapis.com/css2?family=Roboto:ital,wght@0,400;0,700;1,400&display=swap" rel="stylesheet">
<style>
  :root {
    --page: #e4e4e4;
    --card-dark: #000000;
    --card-light: #ffffff;
    --ink-light: #ffffff;
    --ink-dark: #111111;
    --ink-muted: #555555;
    --accent-blue: #1aa3e8;
    --accent-red: #e8231a;
    --accent-orange: #f26a1b;
  }
  * { box-sizing: border-box; margin: 0; padding: 0; }
  html, body {
    width: 1125px; height: 1200px; overflow: hidden;
    background: var(--page);
    font-family: "Roboto", Arial, sans-serif;
  }
  .card {
    position: absolute; left: 171px; width: 826px; height: 470px;
    box-shadow: 0 4px 10px rgba(0,0,0,0.25);
    text-align: center;
  }
  .card--front { top: 106px; background: var(--card-dark); color: var(--ink-light); }
  .card--back { top: 639px; background: var(--card-light); color: var(--ink-muted); }

  .brand {
    position: absolute; left: 0; right: 0;
    display: flex; align-items: center; justify-content: center; gap: 12px;
    font-weight: 700; letter-spacing: 1px; line-height: 1;
  }
  .brand__dot { border-radius: 50%; background: var(--accent-blue); flex: none; }
  .brand__square { background: var(--accent-red); flex: none; }

  .card--front .brand--top { top: 100px; font-size: 32px; color: var(--ink-light); }
  .card--front .brand--top .brand__dot { width: 24px; height: 24px; }
  .card--front .brand--bottom { top: 336px; font-size: 26px; letter-spacing: 4px; color: var(--accent-orange); }
  .card--front .brand--bottom .brand__square { width: 20px; height: 20px; }

  .card--back .brand { top: 146px; font-size: 42px; color: var(--ink-dark); }
  .card--back .brand__dot { width: 30px; height: 30px; }
  .brand-sub {
    position: absolute; left: 0; right: 0; top: 196px;
    font-size: 12px; font-weight: 700; letter-spacing: 9px; color: var(--ink-muted);
  }

  .contact { position: absolute; left: 0; right: 0; top: 173px; }
  .contact__name { font-size: 29px; font-weight: 700; line-height: 36px; margin-bottom: 6px; }
  .contact__line { font-size: 19.5px; line-height: 26.5px; }

  .services { position: absolute; left: 0; right: 0; top: 314px; font-size: 19.5px; line-height: 24.5px; }
  .services__sep { color: var(--accent-blue); }
  .thanks { position: absolute; left: 0; right: 0; top: 397px; font-size: 19.5px; font-style: italic; color: var(--accent-orange); }
</style>
</head>
<body>
  <section class="card card--front">
    <div class="brand brand--top"><span class="brand__dot"></span>PINEGROVE</div>
    <div class="contact">
      <p class="contact__name">Teodor K (Ted)</p>
      <p class="contact__line">(P) 555.284.9136</p>
      <p class="contact__line">Pinegrovehvac47@mailbox-example.com</p>
      <p class="contact__line">www.Pinegrovehvac.com</p>
    </div>
    <div class="brand brand--bottom"><span class="brand__square"></span>HEATING &amp; COOLING</div>
  </section>

  <section class="card card--back">
    <div class="brand"><span class="brand__dot"></span>PINEGROVE</div>
    <p class="brand-sub">HEATING &amp; COOLING</p>
    <div class="services">
      <p>Repairs, Installations, &amp; maintenance</p>
      <p>Quality work at reasonable prices <span class="services__sep">&bull;</span> Residential/commercial</p>
      <p>Licensed &amp; Insured</p>
    </div>
    <p class="thanks">Thank you for your business &amp; refferal</p>
  </section>
</body>
</html>
```